Menu Design for Indian Restaurant

We are a new Indian restaurant, named Saffron Lantern Restaurant, looking for a sophisticated looking menu. It is a semi-formal dining restaurant with wooden tables and chairs and will have a focus on a creating a lively atmosphere. Environment-friendly products will be used, and the menu will be 100% vegetarian. There will be an emphasis on fresh, healthy and delicious food. We will be targeting vegans, vegetarians, health conscious people, people from all age groups, Indians, Australian's as well as other ethnic communities. We need a clean, simple, sophisticated design for the new restaurant menu. Attached is the restaurant logo for reference.

UPDATE:
- We have attached the menu
- We are not looking for any particular type of layout or size (open to suggests). Please suggest this after having a look at the menu contents. However, we will be having one formal menu to be used in the restaurant, and one in brochure form for distribution.
- There are no images at present. If you feel the need of images, please use sample images for now.

Thank you for the entries thus far.
Updates

Target Market(s)

All age groups from different nationalities

Industry/Entity Type

Indian Restaurant

Colors

Designer to choose colors to be used in the design.

Requirements
Nice to have
• This will be printed on environmentally friendly paper.

```html
<!DOCTYPE html>
<html lang="en">
<head>
<meta charset="utf-8">
<title>Saffron Lantern Restaurant – Menu Spread</title>
<link rel="stylesheet" href="https://fonts.googleapis.com/css2?family=Cherry+Swash:wght@700&family=Open+Sans:wght@400;700&family=Italianno&display=swap">
<style>
  :root {
    --backdrop: #dcdcdc;
    --paper: #f7edd2;
    --paper-edge: #eadcb8;
    --saffron: #ef8a22;
    --saffron-deep: #e3761a;
    --leaf: #2f9b3a;
    --leaf-deep: #1f7d2b;
    --heading: #7b4a1f;
    --ink: #2b2118;
    --ink-soft: #5c5146;
    --white: #ffffff;
  }
  * { box-sizing: border-box; margin: 0; padding: 0; }
  html, body { width: 1200px; height: 850px; overflow: hidden; }
  body { background: var(--backdrop); font-family: "Open Sans", Arial, sans-serif; color: var(--ink); position: relative; }

  .menu-spread {
    position: absolute; left: 50px; top: 35px; width: 1100px; height: 780px;
    display: flex; box-shadow: 0 6px 18px rgba(0,0,0,.22);
  }
  .menu-page { position: relative; width: 550px; height: 780px; background: var(--paper); overflow: hidden; }
  .menu-page--left { box-shadow: inset -10px 0 14px -10px rgba(0,0,0,.25); }
  .menu-page--right { box-shadow: inset 10px 0 14px -10px rgba(0,0,0,.2); }

  .foliage-top {
    position: absolute; left: 0; top: 0; width: 100%; height: 105px;
    background: linear-gradient(180deg, var(--saffron) 0%, var(--saffron) 55%, rgba(239,138,34,.55) 80%, rgba(239,138,34,0) 100%);
  }
  .foliage-bottom {
    position: absolute; left: 0; bottom: 0; width: 100%; height: 95px;
    background: linear-gradient(0deg, var(--leaf-deep) 0%, var(--leaf) 55%, rgba(47,155,58,.5) 82%, rgba(47,155,58,0) 100%);
  }

  .brand {
    position: absolute; top: 44px; display: flex; align-items: center; gap: 6px;
    font-family: "Open Sans", Arial, sans-serif; font-weight: 700; font-size: 14px; color: var(--leaf-deep);
    background: var(--paper); padding: 4px 10px; border-radius: 3px;
  }
  .brand-dot { width: 10px; height: 10px; border-radius: 50%; background: var(--saffron-deep); }
  .menu-page--left .brand { right: 40px; }
  .menu-page--right .brand { left: 40px; }

  .section-title {
    font-family: "Cherry Swash", Georgia, serif; font-weight: 700; font-size: 25px;
    color: var(--heading); letter-spacing: 2px; text-shadow: 1px 1px 0 rgba(0,0,0,.12);
  }

  .food-photo { position: absolute; border-radius: 50%; opacity: .45; }
  .photo-dosa { left: 180px; top: 230px; width: 260px; height: 270px;
    background: radial-gradient(ellipse at 40% 40%, #e8b56a 0%, #d9a05a 40%, #efe1c4 75%, rgba(247,237,210,0) 100%); }
  .photo-soup { left: 40px; top: 118px; width: 180px; height: 120px;
    background: radial-gradient(ellipse, #e6c88a 0%, #f3ead4 60%, rgba(247,237,210,0) 100%); opacity: .7; }
  .photo-kebab { left: 330px; top: 300px; width: 200px; height: 180px;
    background: radial-gradient(ellipse, #8a9a4a 0%, #b8b07a 40%, #efe6cf 75%, rgba(247,237,210,0) 100%); opacity: .6; }

  .menu-section { position: absolute; z-index: 2; }
  .breakfast { left: 55px; top: 118px; width: 300px; }
  .soup { left: 200px; top: 112px; width: 300px; }
  .entree { left: 40px; top: 218px; width: 440px; }
  .breakfast .section-title { margin: 0 0 14px 70px; }
  .soup .section-title { margin: 0 0 8px 60px; }
  .entree .section-title { margin: 0 0 10px 180px; }

  .menu-item { margin-bottom: 9px; }
  .item-line { display: flex; align-items: baseline; gap: 3px; font-size: 11px; font-weight: 700; }
  .item-line .note { font-weight: 400; font-size: 7.5px; color: var(--ink-soft); white-space: nowrap; }
  .item-leader { flex: 1; border-bottom: 1px dotted var(--ink); transform: translateY(-3px); min-width: 20px; }
  .item-price { font-weight: 700; }
  .item-desc { font-size: 8.5px; color: var(--ink-soft); margin-top: 1px; }
  .entree .menu-item { margin-bottom: 11px; width: 300px; }
  .soup .menu-item { margin-bottom: 3px; }
  .soup .item-line { font-size: 10.5px; }

  .tagline {
    position: absolute; right: 26px; bottom: 14px; z-index: 2;
    font-family: "Italianno", cursive; font-size: 30px; color: var(--white); letter-spacing: 1px;
  }
</style>
</head>
<body>
<main class="menu-spread">
  <section class="menu-page menu-page--left">
    <div class="foliage-top" role="img" aria-label="Orange foliage border along the top edge"></div>
    <div class="brand"><span class="brand-dot"></span>Saffron Lantern</div>
    <div class="food-photo photo-dosa" role="img" aria-label="Faded photo of a rolled dosa with sambar and chutney bowls"></div>

    <div class="menu-section breakfast">
      <h2 class="section-title">Breakfast</h2>
      <div class="menu-item"><div class="item-line">Dosa/ Vada/ Idli <span class="note">served with sambar, coconut &amp; tomato chutney</span><span class="item-leader"></span><span class="item-price">$11.9</span></div><p class="item-desc">Crispy crepe made with ground rice and lentils gluten free.</p></div>
      <div class="menu-item"><div class="item-line">Rava Dosa<span class="item-leader"></span><span class="item-price">$9.9</span></div><p class="item-desc">Crispy crepe made with semolina and lentil and onion stuffed with potatoes.</p></div>
      <div class="menu-item"><div class="item-line">Kanda Rava Dosa<span class="item-leader"></span><span class="item-price">$11.9</span></div><p class="item-desc">Crispy crepe made with ground rice and lentil stuffed with potatoes.</p></div>
      <div class="menu-item"><div class="item-line">Masala Rava Dosa<span class="item-leader"></span><span class="item-price">$11.9</span></div><p class="item-desc">Crispy crepe made with rice and lentil batter with clarified butter.</p></div>
      <div class="menu-item"><div class="item-line">Dosa/ Vada/ Idli <span class="note">served with sambar, coconut &amp; tomato chutney</span><span class="item-leader"></span><span class="item-price">$11.9</span></div><p class="item-desc">Crispy crepe made with ground rice and lentils gluten free.</p></div>
      <div class="menu-item"><div class="item-line">Rava Dosa<span class="item-leader"></span><span class="item-price">$11.9</span></div><p class="item-desc">Crispy crepe made with ground rice and lentil stuffed with potatoes.</p></div>
      <div class="menu-item"><div class="item-line">Kanda Rava Dosa<span class="item-leader"></span><span class="item-price">$11.9</span></div><p class="item-desc">Crispy crepe made with ground rice and lentils gluten free.</p></div>
      <div class="menu-item"><div class="item-line">Masala Rava Dosa<span class="item-leader"></span><span class="item-price">$11.9</span></div><p class="item-desc">Crispy crepe made with rice and lentil batter with clarified butter.</p></div>
      <div class="menu-item"><div class="item-line">Dosa/ Vada/ Idli <span class="note">served with sambar, coconut &amp; tomato chutney</span><span class="item-leader"></span><span class="item-price">$11.9</span></div><p class="item-desc">Crispy crepe made with ground rice and lentils gluten free.</p></div>
      <div class="menu-item"><div class="item-line">Rava Dosa<span class="item-leader"></span><span class="item-price">$9.9</span></div><p class="item-desc">Crispy crepe made with semolina and lentil and onion stuffed with potatoes.</p></div>
      <div class="menu-item"><div class="item-line">Kanda Rava Dosa<span class="item-leader"></span><span class="item-price">$11.9</span></div><p class="item-desc">Crispy crepe made with ground rice and lentil stuffed with potatoes.</p></div>
      <div class="menu-item"><div class="item-line">Masala Rava Dosa<span class="item-leader"></span><span class="item-price">$11.9</span></div><p class="item-desc">Crispy crepe made with rice and lentil batter with clarified butter.</p></div>
    </div>

    <div class="foliage-bottom" role="img" aria-label="Green foliage border along the bottom edge"></div>
  </section>

  <section class="menu-page menu-page--right">
    <div class="foliage-top" role="img" aria-label="Orange foliage border along the top edge"></div>
    <div class="brand"><span class="brand-dot"></span>Saffron Lantern</div>
    <div class="food-photo photo-soup" role="img" aria-label="Photo of a bowl of creamy soup"></div>
    <div class="food-photo photo-kebab" role="img" aria-label="Faded photo of green hara kebabs with onion rings"></div>

    <div class="menu-section soup">
      <h2 class="section-title">Soup of the Day</h2>
      <div class="menu-item"><div class="item-line">Cream of tomato with crotons<span class="item-leader"></span><span class="item-price">$4.9</span></div></div>
      <div class="menu-item"><div class="item-line">Curried pumpkin with challots<span class="item-leader"></span><span class="item-price">$4.9</span></div></div>
    </div>

    <div class="menu-section entree">
      <h2 class="section-title">Entree (Tapas)</h2>
      <div class="menu-item"><div class="item-line">Kamal Kofta (4pcs)<span class="item-leader"></span><span class="item-price">$6.9</span></div><p class="item-desc">Lotus stem and paneer dumplings with fresh chilli spice croquets.</p></div>
      <div class="menu-item"><div class="item-line">Hara Kebab (4pcs)<span class="item-leader"></span><span class="item-price">$6.9</span></div><p class="item-desc">Fresh baby spinach ricotta cheese mash potatoes ginger fresh coriander fresh chilli patty.</p></div>
      <div class="menu-item"><div class="item-line">Kamal Kofta (4pcs)<span class="item-leader"></span><span class="item-price">$6.9</span></div><p class="item-desc">Crispy crepe made with ground rice and lentils gluten free.</p></div>
      <div class="menu-item"><div class="item-line">Hara Kebab (4pcs)<span class="item-leader"></span><span class="item-price">$6.9</span></div><p class="item-desc">Fresh baby spinach ricotta cheese mash potatoes ginger fresh coriander fresh chilli patty.</p></div>
      <div class="menu-item"><div class="item-line">Kamal Kofta (4pcs)<span class="item-leader"></span><span class="item-price">$6.9</span></div><p class="item-desc">Crispy crepe made with ground rice and lentils gluten free.</p></div>
      <div class="menu-item"><div class="item-line">Hara Kebab (4pcs)<span class="item-leader"></span><span class="item-price">$6.9</span></div><p class="item-desc">Fresh baby spinach ricotta cheese mash potatoes ginger fresh coriander fresh chilli patty.</p></div>
      <div class="menu-item"><div class="item-line">Kamal Kofta (4pcs)<span class="item-leader"></span><span class="item-price">$6.9</span></div><p class="item-desc">Crispy crepe made with ground rice and lentils gluten free.</p></div>
      <div class="menu-item"><div class="item-line">Hara Kebab (4pcs)<span class="item-leader"></span><span class="item-price">$6.9</span></div><p class="item-desc">Fresh baby spinach ricotta cheese mash potatoes ginger fresh coriander fresh chilli patty.</p></div>
    </div>

    <div class="foliage-bottom" role="img" aria-label="Green foliage border along the bottom edge"></div>
    <p class="tagline">The Essence of Indian Cuisine</p>
  </section>
</main>
</body>
</html>
```